Local fast-growing company in the service sector

We are looking for a modern business card design, which should also appear on our letterheads

Target Market(s)

Private and industrial sectors

Contact Information for Business Card

Vorname Name
Lindkofer Str. 18
71468 Erlenhofen
Tel.: 07163-418259-0
Name@kovaltec-pbz.de

Colors
9d9d9d
919191
aaaaaa

Requirements
Must have
• The logo (file) in silver

```html
<!DOCTYPE html>
<html lang="de">
<head>
<meta charset="utf-8">
<title>Kovaltec – Visitenkarte</title>
<link href="https://fonts.googleapis.com/css2?family=Lato:wght@400;700;900&display=swap" rel="stylesheet">
<style>
  :root {
    --page-bg: #e4e2df;
    --card-white: #ffffff;
    --card-shade: #efefef;
    --silver-dark: #919191;
    --silver-mid: #9d9d9d;
    --silver-light: #aaaaaa;
    --silver-pale: #cfcfcf;
    --text-gray: #7b7b7b;
  }
  * { margin: 0; padding: 0; box-sizing: border-box; }
  html, body {
    width: 1200px; height: 780px; overflow: hidden;
    background: var(--page-bg);
    font-family: "Lato", Arial, sans-serif;
  }
  .canvas { position: relative; width: 1200px; height: 780px; }
  .business-card {
    position: absolute; left: 75px; top: 90px;
    width: 1050px; height: 600px;
    border-radius: 34px; overflow: hidden;
    background: linear-gradient(160deg, var(--card-white) 0%, var(--card-shade) 100%);
    box-shadow: 0 10px 30px rgba(0,0,0,.18);
  }
  .card-waves { position: absolute; inset: 0; }
  .holder-name {
    position: absolute; left: 400px; top: 62px;
    font-size: 32px; font-weight: 700; letter-spacing: 1px;
    color: var(--text-gray); text-transform: uppercase;
  }
  .brand { position: absolute; left: 80px; top: 290px; }
  .brand-row { display: flex; align-items: center; gap: 14px; }
  .brand-square {
    width: 48px; height: 48px; border-radius: 7px;
    background: var(--silver-pale);
  }
  .brand-name {
    font-size: 62px; font-weight: 900; line-height: 1;
    color: var(--silver-light); letter-spacing: -1px;
  }
  .brand-web {
    margin: 6px 0 0 62px;
    font-size: 26px; font-weight: 400; letter-spacing: 1px;
    color: var(--silver-pale);
  }
  .contact {
    position: absolute; right: 64px; top: 120px;
    text-align: right; color: var(--text-gray);
    font-size: 26px; line-height: 1.3; font-style: normal;
  }
  .contact-address { margin-bottom: 36px; }
  .contact-line {
    display: flex; justify-content: flex-end; align-items: center; gap: 14px;
    margin-bottom: 12px;
  }
  .contact-icon { width: 30px; height: 30px; flex: none; }
</style>
</head>
<body>
<main class="canvas">
  <section class="business-card">
    <svg class="card-waves" viewBox="0 0 1050 600" aria-hidden="true">
      <defs>
        <linearGradient id="silverPanel" x1="0" y1="0" x2="1" y2="1">
          <stop offset="0" stop-color="#c2c2c2"/>
          <stop offset="1" stop-color="#d8d8d8"/>
        </linearGradient>
      </defs>
      <path d="M700 0 C620 130 570 260 520 380 C480 470 440 550 380 600 L1050 600 L1050 0 Z" fill="url(#silverPanel)"/>
      <path d="M688 0 C608 130 556 260 506 380 C468 468 428 548 366 600 L380 600 C440 550 480 470 520 380 C570 260 620 130 700 0 Z" fill="#f6f6f6"/>
      <path d="M510 390 C470 480 420 550 340 600 L300 600 C390 550 450 480 510 390 Z" fill="var(--silver-mid)" opacity=".8"/>
      <path d="M470 430 C420 520 340 570 220 600 L270 600 C380 570 440 510 470 430 Z" fill="var(--silver-dark)" opacity=".55"/>
      <path d="M430 480 C370 550 280 585 150 600 L200 600 C320 585 390 550 430 480 Z" fill="var(--silver-light)" opacity=".5"/>
    </svg>

    <h1 class="holder-name">Jonas Keller</h1>

    <div class="brand">
      <div class="brand-row">
        <span class="brand-square"></span>
        <span class="brand-name">KOVALTEC</span>
      </div>
      <p class="brand-web">kovaltec-pbz.de</p>
    </div>

    <address class="contact">
      <p class="contact-address">Lindkofer Str. 18<br>71468 Erlenhofen</p>
      <p class="contact-line">07163-418259-0
        <svg class="contact-icon" viewBox="0 0 30 30" aria-label="Telefon">
          <rect width="30" height="30" rx="6" fill="var(--silver-mid)"/>
          <path d="M10 8 L13 8 L14 12 L12 13.5 C13 16 14 17 16.5 18 L18 16 L22 17 L22 20 C16 21 9 14 10 8 Z" fill="#fff"/>
        </svg>
      </p>
      <p class="contact-line">Name@kovaltec-pbz.de
        <svg class="contact-icon" viewBox="0 0 30 30" aria-label="E-Mail">
          <rect width="30" height="30" rx="6" fill="var(--silver-mid)"/>
          <rect x="7" y="10" width="16" height="11" fill="none" stroke="#fff" stroke-width="1.8"/>
          <path d="M7 10 L15 16 L23 10" fill="none" stroke="#fff" stroke-width="1.8"/>
        </svg>
      </p>
    </address>
  </section>
</main>
</body>
</html>
```